Layout for new page on existing website

We have an existing website (www.brightmillworks.org) and need a new page designing to promote a new product.
The new page needs to be consistent with the existing website look and feel (www.brightmillworks.org) but current persistent elements on the standard page design can be moved/removed from the page to accommodate a new layout necessary for getting all the content laid out in a logical user friendly way.
The content required for the page is attached along with a wireframe mock up that may help understand the expectation, however the wireframe was just created to help me work out what was needed on the page and the layout can be different. A key element is the quality of the design of each of the artifacts (e.g. the panel the embedded video needs to go in, icons etc) and a clear display of the information.
Updates
The website that the new page needs to fit into is www.brightmillworks.org, i will also added the company logo to the brief.
Our Corporate Colours
- Green: #A2FF00
- Cream: #FFFF99
- Yellow: #FFE900
- Grey: #534741

```html
<!DOCTYPE html>
<html lang="en">
<head>
<meta charset="utf-8">
<title>Brightmill Works – Course Management and Booking</title>
<link rel="stylesheet" href="https://fonts.googleapis.com/css2?family=Arimo:wght@700&family=Fira+Sans:wght@400;500;700&family=PT+Sans+Narrow:wght@700&display=swap">
<style>
  :root {
    --green: #A2FF00;
    --green-dark: #6fbf1a;
    --cream: #FFFF99;
    --yellow: #FFE900;
    --grey: #534741;
    --grey-deep: #4a403b;
    --white: #ffffff;
    --ink: #1d1a17;
  }
  * { margin: 0; padding: 0; box-sizing: border-box; }
  html, body { width: 1039px; height: 1200px; overflow: hidden; background: var(--grey); }
  body { font-family: "Fira Sans", sans-serif; color: var(--white); }
  .page { position: relative; width: 1039px; height: 1200px; }
  .page-column {
    position: absolute; left: 107px; top: 150px; width: 826px; height: 1050px;
    background: var(--grey);
    box-shadow: -8px 0 14px rgba(0,0,0,.35), 8px 0 14px rgba(0,0,0,.35);
  }
  .abs { position: absolute; }

  .home-link { left: 160px; top: 62px; width: 50px; text-align: center; font-size: 12px; font-weight: 500; }
  .home-link svg { display: block; margin: 0 auto 10px; }
  .home-link .shadow { width: 90px; height: 8px; margin: -8px 0 0 -20px; border-radius: 50%; background: radial-gradient(rgba(0,0,0,.45), transparent 70%); }

  .brand { left: 300px; top: 78px; width: 540px; display: flex; align-items: center; justify-content: center; gap: 14px; }
  .brand-dot { width: 26px; height: 26px; border-radius: 50%; background: var(--green); }
  .brand-name { font-weight: 700; font-size: 30px; letter-spacing: 6px; color: var(--white); }

  .headline { left: 107px; top: 148px; width: 826px; text-align: center; font-family: "Arimo", sans-serif; font-size: 29px; color: var(--yellow); }

  .hero { left: 135px; top: 208px; width: 768px; height: 246px; background: linear-gradient(90deg, #f4f4f4, #ffffff 45%, #f7f7f7); }
  .quality-seal { left: 816px; top: 196px; }

  .tagline { left: 107px; top: 473px; width: 826px; text-align: center; font-size: 21px; font-weight: 500; }

  .video-panel { left: 135px; top: 525px; width: 332px; height: 247px; background: #000; border: 1px solid #666; }
  .video-play { position: absolute; left: 146px; top: 88px; }
  .video-controls { position: absolute; left: 0; bottom: 0; width: 100%; height: 14px; background: linear-gradient(#eee, #bbb); display: flex; align-items: center; gap: 6px; padding: 0 4px; font-size: 8px; color: #222; }
  .video-track { flex: 1; height: 3px; background: #555; }

  .quote-bar { left: 475px; top: 525px; width: 427px; height: 35px; background: linear-gradient(#b7ff3a, var(--green) 50%, #8ce000); border: 2px solid #4f8a10; box-shadow: 0 0 6px rgba(162,255,0,.6); padding: 4px 12px; font-family: "PT Sans Narrow", sans-serif; font-size: 19px; color: var(--ink); }
  .quote-text { left: 487px; top: 580px; width: 400px; font-size: 13px; line-height: 17.6px; color: var(--cream); font-weight: 500; }
  .quote-author { left: 487px; top: 662px; font-size: 13px; font-weight: 500; }

  .features-title { left: 135px; top: 797px; font-family: "PT Sans Narrow", sans-serif; font-size: 24px; color: var(--green); }

  .feature { position: absolute; width: 380px; }
  .feature-icon { position: absolute; top: -13px; }
  .feature-name { position: absolute; top: -9px; font-size: 15px; font-weight: 700; color: var(--yellow); white-space: nowrap; }
  .feature-text { position: absolute; top: 19px; left: 0; width: 380px; font-size: 11.5px; line-height: 16.6px; }
  .col-left { left: 135px; }
  .col-left .feature-name { left: 50px; }
  .col-right { left: 555px; }
  .col-right .feature-name { left: 56px; }
  .col-right .feature-icon { left: 6px; }
</style>
</head>
<body>
<main class="page">
  <div class="page-column"></div>

  <a class="abs home-link">
    <svg width="44" height="40" viewBox="0 0 44 40" aria-hidden="true">
      <path d="M4 20 L22 4 L40 20" fill="none" stroke="#f0c419" stroke-width="4" stroke-linejoin="round"/>
      <path d="M9 18 V36 H35 V18" fill="none" stroke="#f0c419" stroke-width="3.5"/>
      <rect x="18" y="24" width="8" height="12" fill="none" stroke="#f0c419" stroke-width="3"/>
    </svg>
    <div class="shadow"></div>
    Home
  </a>

  <div class="abs brand">
    <span class="brand-dot"></span>
    <span class="brand-name">BRIGHTMILL WORKS</span>
  </div>

  <h1 class="abs headline">COURSE MANAGEMENT AND BOOKING SIMPLIFIED</h1>

  <div class="abs hero" role="img" aria-label="Photo of a young woman lying down reading a book beside a stack of colourful books"></div>
  <svg class="abs quality-seal" width="104" height="104" viewBox="0 0 104 104" aria-hidden="true">
    <circle cx="52" cy="52" r="50" fill="#f7c600"/>
    <circle cx="52" cy="52" r="38" fill="#d81e1e"/>
  </svg>

  <p class="abs tagline">Built with only your busiess in mind</p>

  <div class="abs video-panel">
    <svg class="video-play" width="48" height="48" viewBox="0 0 48 48" aria-label="Play video">
      <circle cx="24" cy="24" r="23" fill="#5aa51a" stroke="#9ee04a" stroke-width="2"/>
      <path d="M18 13 L35 24 L18 35 Z" fill="#fff"/>
    </svg>
    <div class="video-controls"><span>▶</span><span>00:00</span><span class="video-track"></span><span>00:20</span></div>
  </div>

  <h2 class="abs quote-bar">CUSTOMER QUOTE</h2>
  <p class="abs quote-text">A convenient tool that was simple to integrate into our website. It has allowed both the business and our customers an easy way to book courses. In life sometimes simple is good and this is a great example!"</p>
  <p class="abs quote-author">Clara Benton, Director @ TutorPath www.tutorpath.org</p>

  <h2 class="abs features-title">KEY FEATURES</h2>

  <div class="feature col-left" style="top:862px">
    <svg class="feature-icon" style="left:0" width="36" height="36" viewBox="0 0 36 36" aria-hidden="true">
      <path d="M28 12 A12 12 0 1 0 30 22" fill="none" stroke="#eee" stroke-width="6"/>
      <path d="M22 4 L34 6 L30 16 Z" fill="#eee"/>
    </svg>
    <h3 class="feature-name">Available and Easy to Use 24/7</h3>
    <p class="feature-text">By allowing booking and payment at any time of the day, your attendees will be more likely to commit to your event and with no account setup or password required and no paper forms to fill in and post, booking onto and paying for your courses is easy.</p>
  </div>

  <div class="feature col-left" style="top:967px">
    <svg class="feature-icon" style="left:0" width="36" height="32" viewBox="0 0 36 32" aria-hidden="true">
      <rect x="2" y="2" width="32" height="22" fill="#333" stroke="#ddd" stroke-width="3"/>
      <rect x="12" y="25" width="12" height="4" fill="#ddd"/>
    </svg>
    <h3 class="feature-name">Online Course Promotion</h3>
    <p class="feature-text" style="top:23px">List your upcoming courses in a clear and simple way so people can easily find and select the course that suits them.</p>
  </div>

  <div class="feature col-left" style="top:1050px">
    <svg class="feature-icon" style="left:0;top:-18px" width="32" height="38" viewBox="0 0 32 38" aria-hidden="true">
      <path d="M11 2 H21 L18 8 H14 Z" fill="#6aa832"/>
      <circle cx="16" cy="23" r="14" fill="#6aa832"/>
      <text x="16" y="30" font-family="Arial, sans-serif" font-size="18" font-weight="700" text-anchor="middle" fill="#fff">$</text>
    </svg>
    <h3 class="feature-name">Online &amp; Offline Payments</h3>
    <p class="feature-text" style="top:16px">Take payments online, whilst having the flexibility of managing and adding offline payments.</p>
  </div>

  <div class="feature col-left" style="top:1130px">
    <svg class="feature-icon" style="left:0;top:-18px" width="34" height="34" viewBox="0 0 34 34" aria-hidden="true">
      <g fill="none" stroke="#ddd" stroke-width="2.5">
        <rect x="2" y="2" width="30" height="30"/>
        <path d="M12 2 V32 M22 2 V32 M2 12 H32 M2 22 H32"/>
      </g>
    </svg>
    <h3 class="feature-name">Venue Database Management</h3>
    <p class="feature-text" style="top:18px">Easily add, edit and remove venues from which you operate your courses from.</p>
  </div>

  <div class="feature col-right" style="top:862px">
    <svg class="feature-icon" style="left:0;top:-24px" width="42" height="40" viewBox="0 0 42 40" aria-hidden="true">
      <rect x="2" y="12" width="38" height="26" rx="2" fill="#f0b21c"/>
      <rect x="9" y="4" width="24" height="20" fill="#fff" stroke="#9bb" stroke-width="1"/>
      <path d="M13 10 H29 M13 14 H29 M13 18 H25" stroke="#48a" stroke-width="1.5"/>
      <path d="M2 14 L21 28 L40 14 V38 H2 Z" fill="#f7c63a"/>
    </svg>
    <h3 class="feature-name">Built in Email System</h3>
    <p class="feature-text" style="top:18px">Enable quick and easy communication with upcoming course candidates and promotion of additional courses to past candidates.</p>
  </div>

  <div class="feature col-right" style="top:948px">
    <svg class="feature-icon" style="left:0;top:-20px" width="42" height="36" viewBox="0 0 42 36" aria-hidden="true">
      <rect x="2" y="2" width="38" height="30" rx="3" fill="#fff" stroke="#bbb"/>
      <rect x="6" y="6" width="30" height="22" fill="#5b9e2c"/>
      <path d="M10 26 L32 8" stroke="#ddd" stroke-width="4" stroke-linecap="round"/>
    </svg>
    <h3 class="feature-name">Customisable Look and Feel</h3>
    <p class="feature-text" style="top:17px">All elements of the booking systems design will fit in with your existing websites style.</p>
  </div>

  <div class="feature col-right" style="top:1035px">
    <svg class="feature-icon" style="left:2px;top:-24px" width="40" height="38" viewBox="0 0 40 38" aria-hidden="true">
      <path d="M20 2 L38 18 H33 V36 H7 V18 H2 Z" fill="#6aa832"/>
      <path d="M20 6 L34 18 H6 Z" fill="#3f7e1c"/>
      <rect x="10" y="18" width="20" height="18" fill="#f2f2f2"/>
      <rect x="17" y="24" width="6" height="12" fill="#6aa832"/>
    </svg>
    <h3 class="feature-name">Live Course Place Availability</h3>
    <p class="feature-text" style="top:22px">By defining minimum and maximum candidates permitted on a course its easy to prevent overbooking and also prevent courses running that don't have enough candidates.</p>
  </div>
</main>
</body>
</html>
```